Pitch Deck Redesign

We are a company in the ed-tech/gaming business wishing to fine-tune the looks of our pitch deck/company presentation.
Attached is the current template we use. And while we want to keep the headlines, general structure and the flow represented in various graphs, we want a design whizz to fine-tune the looks of it, updating graphics and add a bit more graphics. In the end we basically want to give the template a professional edge while still conveying the design philosophy we're trying to achieve, the philosophy is as follows:
A combination of education and playfulness/digital entertainment (particularly gaming). It should additionally be clean, not cluttered yet with a hint of fun.
We of course want to be able to simply ad our own texts as well as our to logo various elements

```html
<!DOCTYPE html>
<html lang="en">
<head>
<meta charset="utf-8">
<title>Quizora — Pitch Deck</title>
<link href="https://fonts.googleapis.com/css2?family=Poppins:wght@400;500;600;700;800&display=swap" rel="stylesheet">
<style>
  :root{
    --teal:#00b5c6;
    --yellow:#fec524;
    --yellow-soft:#ffd54a;
    --pink:#f0447f;
    --pink-soft:#ff7aa6;
    --ink:#3b3b3b;
    --muted:#6b6b6b;
    --brand-blue:#1769c1;
    --white:#ffffff;
  }
  *{box-sizing:border-box;margin:0;padding:0}
  html,body{width:1200px;height:2800px;overflow:hidden;background:var(--white)}
  body{position:relative;font-family:"Poppins",sans-serif;color:var(--ink)}
  .slide{position:absolute;left:265px;width:670px;height:376px;background:var(--white);overflow:hidden;box-shadow:0 2px 6px rgba(0,0,0,.18)}
  .shape{position:absolute;left:0;top:0;width:670px;height:376px}
  .photo{position:absolute;overflow:hidden;box-shadow:0 8px 18px rgba(0,0,0,.12)}
  .photo.room{background:
      radial-gradient(ellipse at 65% 55%,rgba(246,238,228,.9) 0%,rgba(246,238,228,0) 45%),
      radial-gradient(ellipse at 20% 70%,rgba(168,134,104,.75) 0%,rgba(168,134,104,0) 50%),
      linear-gradient(165deg,#e7e3de 0%,#d9cdbf 45%,#b99c80 80%,#8f735c 100%)}
  .photo.sofa{background:
      radial-gradient(ellipse at 45% 55%,rgba(240,236,230,.85) 0%,rgba(240,236,230,0) 40%),
      radial-gradient(ellipse at 85% 40%,rgba(205,120,96,.8) 0%,rgba(205,120,96,0) 50%),
      linear-gradient(150deg,#e9dccd 0%,#b58a72 45%,#6d4a3b 100%)}
  .photo.arcade{background:
      radial-gradient(circle at 55% 38%,rgba(22,70,120,.95) 0%,rgba(22,70,120,0) 28%),
      radial-gradient(ellipse at 30% 90%,rgba(226,66,44,.85) 0%,rgba(226,66,44,0) 45%),
      radial-gradient(ellipse at 70% 10%,rgba(222,110,70,.8) 0%,rgba(222,110,70,0) 40%),
      linear-gradient(160deg,#3a9ab8 0%,#2a86a6 50%,#1f6f93 100%)}
  .eyebrow{position:absolute;font-size:11px;font-weight:400;color:var(--muted)}
  .headline{position:absolute;font-weight:700;line-height:1.2;color:var(--ink)}
  .headline .accent{color:var(--pink)}
  .body-copy{position:absolute;font-size:6.4px;line-height:15px;color:var(--ink)}
  .item-title{font-size:8.5px;font-weight:600;color:var(--ink);margin-bottom:6px}
  .item-text{font-size:6.4px;line-height:14px;color:var(--ink)}
  .footer-mark{position:absolute;left:26px;top:343px;font-size:7px;font-weight:700;color:var(--pink)}
  .footer-note{position:absolute;left:570px;top:343px;font-size:6.4px;color:var(--muted)}
  .brand-name{position:absolute;left:40px;top:165px;font-size:58px;font-weight:800;color:var(--brand-blue);letter-spacing:2px;line-height:1}
  .tagline{position:absolute;left:112px;top:233px;font-size:11px;font-weight:500;color:var(--ink)}
  .info-pill{position:absolute;left:31px;top:211px;width:373px;height:97px;border-radius:49px;background:linear-gradient(90deg,var(--pink-soft),var(--pink));display:flex;align-items:center;padding:0 34px 0 36px;gap:28px;box-shadow:0 6px 14px rgba(240,68,127,.3)}
  .info-pill p{font-size:6.4px;line-height:16px;color:var(--white)}
  .blocks-icon{flex:none;width:44px;height:44px}
</style>
</head>
<body>

<section class="slide" style="top:12px">
  <svg class="shape" viewBox="0 0 670 376"><path d="M273 0H670V376H273C348 300 350 90 273 0Z" fill="var(--teal)"/></svg>
  <div class="brand-name">Quizora</div>
  <div class="tagline">Tagline Here</div>
</section>

<section class="slide" style="top:412px">
  <svg class="shape" viewBox="0 0 670 376"><path d="M0 0H150C142 20 110 26 70 28C35 30 28 55 24 72C20 86 8 94 0 95Z" fill="var(--teal)"/></svg>
  <div class="photo room" role="img" aria-label="Photo of a girl writing in a notebook at a low table" style="left:49px;top:51px;width:200px;height:274px;border-radius:32px"></div>
  <div class="eyebrow" style="left:308px;top:86px">About Us</div>
  <h1 class="headline" style="left:306px;top:112px;font-size:27px;line-height:33px"><span class="accent">We are a company in</span><br>the ed-tech/gaming<br>business</h1>
  <p class="body-copy" style="left:308px;top:230px;width:300px">We build playful learning tools that turn daily study into a game. Teachers, artists and developers work side by side so every lesson feels like a level worth beating, with clear progress and fair rewards. Families can follow each step from any device and celebrate small wins together.</p>
  <div class="footer-mark">Lumo</div>
  <div class="footer-note">Presentation Template</div>
</section>

<section class="slide" style="top:812px">
  <div class="shape" style="width:404px;background:linear-gradient(160deg,var(--yellow) 0%,var(--yellow-soft) 100%)"></div>
  <div class="photo sofa" role="img" aria-label="Photo of a father and son looking at a phone on a sofa" style="left:404px;top:0;width:266px;height:376px;box-shadow:none"></div>
  <div class="eyebrow" style="left:74px;top:68px;color:var(--ink)">About Us</div>
  <h1 class="headline" style="left:72px;top:92px;font-size:37px;line-height:46px">Dedicated To<br>Excellence</h1>
  <p class="body-copy" style="left:74px;top:208px;width:268px">Quality sits at the heart of every product we ship. Each game is tested with real classrooms, reviewed by educators and tuned until the challenge feels just right. We measure learning, not screen time, and we share those results openly with schools and parents.</p>
  <p class="body-copy" style="left:74px;top:279px;width:268px">Small steps, steady progress and plenty of fun keep young learners coming back every day.</p>
  <div class="footer-mark" style="color:var(--ink)">Lumo</div>
</section>

<section class="slide" style="top:1212px">
  <svg class="shape" viewBox="0 0 670 376"><path d="M450 0H670V130C652 124 640 104 640 72C640 42 612 30 565 30C515 30 470 22 450 0Z" fill="var(--yellow)"/></svg>
  <div class="photo arcade" role="img" aria-label="Close-up photo of an arcade joystick on a colourful game panel" style="left:415px;top:50px;width:200px;height:274px;border-radius:32px"></div>
  <h1 class="headline" style="left:72px;top:72px;font-size:37px;line-height:46px"><span class="accent">The Future</span><br>Begins Here</h1>
  <div style="position:absolute;left:72px;top:190px;width:140px">
    <div class="item-title">A Family Of Learning</div>
    <div class="item-text">Short lessons wrapped in quests that reward curiosity.</div>
  </div>
  <div style="position:absolute;left:232px;top:190px;width:140px">
    <div class="item-title">A Family Of Learning</div>
    <div class="item-text">Live progress maps for teachers and for parents.</div>
  </div>
  <div style="position:absolute;left:72px;top:258px;width:140px">
    <div class="item-title">A Family Of Learning</div>
    <div class="item-text">Safe multiplayer rooms built for classmates and friends.</div>
  </div>
  <div style="position:absolute;left:232px;top:258px;width:140px">
    <div class="item-title">A Family Of Learning</div>
    <div class="item-text">Content aligned with school goals in every grade.</div>
  </div>
  <div class="footer-mark">Lumo</div>
  <div class="footer-note">Presentation Template</div>
</section>

<section class="slide" style="top:1612px">
  <svg class="shape" viewBox="0 0 670 376">
    <path d="M430 0H670V14C600 14 545 42 492 42C462 42 442 22 430 0Z" fill="var(--yellow)"/>
    <path d="M0 282C32 294 52 330 82 340C150 362 250 330 322 350C345 358 380 368 386 376H0Z" fill="var(--yellow)"/>
  </svg>
  <div class="photo room" role="img" aria-label="Photo of a girl writing at a table" style="left:47px;top:49px;width:248px;height:128px;border-radius:24px"></div>
  <div class="photo sofa" role="img" aria-label="Photo of a boy using a phone on a sofa" style="left:47px;top:200px;width:248px;height:128px;border-radius:24px"></div>
  <div class="eyebrow" style="left:339px;top:64px">About Us</div>
  <h1 class="headline" style="left:338px;top:86px;font-size:37px;line-height:46px"><span class="accent">A Great Place</span><br>For Education</h1>
  <div style="position:absolute;left:339px;top:204px;width:270px">
    <div class="item-title">A Family Of Learning</div>
    <div class="item-text">Our platform mixes reading, maths and science into short playful missions that fit any timetable and keep every pupil motivated from start to finish.</div>
  </div>
  <div style="position:absolute;left:339px;top:266px;width:270px">
    <div class="item-title">A Family Of Learning</div>
    <div class="item-text">Teachers plan lessons in minutes, assign challenges with one click and see which skills need more practice before the next class begins.</div>
  </div>
  <div class="footer-mark" style="color:var(--ink)">Lumo</div>
  <div class="footer-note">Presentation Template</div>
</section>

<section class="slide" style="top:2012px">
  <svg class="shape" viewBox="0 0 670 376">
    <path d="M0 0H222C200 12 150 10 112 26C62 48 62 100 0 112Z" fill="var(--yellow)"/>
    <path d="M495 0H670V48C620 48 560 40 522 25C506 18 498 8 495 0Z" fill="var(--yellow)"/>
    <path d="M600 376C612 350 640 340 670 332V376Z" fill="var(--yellow)"/>
  </svg>
  <div class="photo room" role="img" aria-label="Photo of a girl writing in a notebook" style="left:365px;top:48px;width:305px;height:280px;border-radius:36px 0 0 36px"></div>
  <div class="eyebrow" style="left:74px;top:76px">About Us</div>
  <h1 class="headline" style="left:70px;top:99px;font-size:37px;line-height:46px"><span class="accent">Your title</span><br>goes here</h1>
  <div class="info-pill">
    <svg class="blocks-icon" viewBox="0 0 44 44" fill="none" stroke="#ffffff" stroke-width="1.6" aria-hidden="true">
      <rect x="13" y="3" width="18" height="18" rx="2"/>
      <rect x="3" y="23" width="18" height="18" rx="2"/>
      <rect x="23" y="23" width="18" height="18" rx="2"/>
      <text x="22" y="16" font-family="Poppins, sans-serif" font-size="10" fill="#ffffff" stroke="none" text-anchor="middle">1</text>
      <text x="12" y="36" font-family="Poppins, sans-serif" font-size="10" fill="#ffffff" stroke="none" text-anchor="middle">2</text>
      <text x="32" y="36" font-family="Poppins, sans-serif" font-size="10" fill="#ffffff" stroke="none" text-anchor="middle">3</text>
    </svg>
    <p>Every learner gets a personal path with levels, badges and friendly hints, so practice feels like play and progress is easy to see.</p>
  </div>
  <div class="footer-mark">Lumo</div>
  <div class="footer-note">Presentation Template</div>
</section>

<section class="slide" style="top:2412px">
  <svg class="shape" viewBox="0 0 670 376"><path d="M0 0H276C270 30 232 50 182 46C122 40 62 40 36 60C16 80 36 120 30 150C25 180 10 196 0 200Z" fill="var(--yellow)"/></svg>
  <div class="photo sofa" role="img" aria-label="Photo of a boy with his father looking at a phone" style="left:277px;top:50px;width:166px;height:274px;border-radius:28px"></div>
  <div class="photo arcade" role="img" aria-label="Close-up photo of an arcade joystick" style="left:459px;top:50px;width:166px;height:274px;border-radius:28px"></div>
  <div class="eyebrow" style="left:55px;top:83px">About Us</div>
  <h1 class="headline" style="left:54px;top:104px;font-size:37px;line-height:46px"><span class="accent">Imagine</span><br>Greatness</h1>
  <p class="body-copy" style="left:55px;top:240px;width:190px">We imagine classrooms where games open doors to big ideas. Every quest builds real skills, every win builds confidence, and every child finds a reason to keep learning.</p>
  <div class="footer-mark">Lumo</div>
  <div class="footer-note">Presentation Template</div>
</section>

</body>
</html>
```